Stonefield Partners Business Card Design

We are looking for a new business card design, we are not happy with our current design. We are a boutique management consulting firm and our clients are typically fortune 500 companies.

I have attached the current front and back that we have as well as a version of our logo that can be used. I am trying to get a higher resolution version of the logo file to upload to the project.

Target Market(s)

Fortune 500 companies are our primary client base. Financial services, life sciences, pharmaceuticals and telecom companies are

Industry/Entity Type

Management Consulting

Contact Information for Business Card

We are trying to communicate a high degree of professionalism, a somewhat minimalist perhaps with some air of whimsy (without overdoing it). Attached is the current design, front and back as well as logos. I like the current back of the card and assume we will keep the phrase the same.

From a color palette perspective, I prefer to stay with a gray scale as they are today.

Font styles to use
Sans Serif

Colors
1b1b1b
474747
ffffff

Requirements
Must have
• Two sided business card design. File format should be something that can be used outside of Photoshop like MS Publisher so that they can be edited with personal information.
• Font should be calibri or something very similar and should be available within MS Office
Should not have
• No other logos or graphics outside of the logo provided.

```html
<!DOCTYPE html>
<html lang="en">
<head>
<meta charset="utf-8">
<title>Stonefield Partners Business Cards</title>
<link rel="stylesheet" href="https://fonts.googleapis.com/css2?family=Arimo:ital,wght@0,400;0,500;0,700;1,400&display=swap">
<style>
  :root {
    --ink: #1b1b1b;
    --grey: #474747;
    --paper: #ffffff;
    --backdrop: #d2d3d7;
  }
  * { margin: 0; padding: 0; box-sizing: border-box; }
  html, body { width: 1098px; height: 1200px; overflow: hidden; }
  body {
    position: relative;
    background: var(--backdrop);
    font-family: "Arimo", Arial, sans-serif;
    color: var(--ink);
  }
  .card {
    position: absolute;
    background: var(--paper);
  }
  .card-front { left: 250px; top: 166px; width: 612px; height: 349px; }
  .card-back  { left: 250px; top: 653px; width: 619px; height: 353px; }

  .brand-band {
    position: absolute; left: 0; top: 120px; width: 100%; height: 108px;
    background: var(--ink);
    display: flex; align-items: center; justify-content: center;
  }
  .brand-name {
    color: var(--paper);
    font-size: 58px; font-weight: 500; letter-spacing: 0.5px;
    display: flex; align-items: center; gap: 14px;
  }
  .brand-dot {
    width: 30px; height: 30px; border-radius: 50%;
    background: var(--paper);
  }
  .tagline {
    position: absolute; left: 0; width: 100%; top: 236px;
    text-align: center; font-size: 18px;
  }
  .front-web {
    position: absolute; left: 0; width: 100%; top: 290px;
    text-align: center; font-size: 14px; font-weight: 700; letter-spacing: 1.4px;
  }

  .person { position: absolute; left: 37px; top: 44px; }
  .person-name { font-size: 29px; font-weight: 700; letter-spacing: 2.4px; line-height: 1; }
  .person-title, .person-office {
    font-size: 14px; letter-spacing: 1.5px; color: var(--grey); margin-top: 10px;
  }
  .person-title { margin-top: 12px; }
  .person-office { font-style: italic; margin-top: 8px; }

  .contact { position: absolute; left: 37px; top: 200px; }
  .contact p, .office p {
    font-size: 15px; letter-spacing: 1.1px; line-height: 24.5px; color: var(--grey);
  }
  .contact .phone { color: var(--ink); font-size: 16px; font-weight: 500; }

  .office { position: absolute; left: 337px; top: 200px; }
  .office .company { color: var(--ink); font-weight: 700; }

  .mark {
    position: absolute; left: 416px; top: 48px; width: 108px; height: 108px;
    border-radius: 50%; background: var(--grey);
  }
</style>
</head>
<body>
  <section class="card card-front">
    <div class="brand-band">
      <div class="brand-name"><span class="brand-dot"></span>Stonefield</div>
    </div>
    <p class="tagline">The trusted partner for leadership’s boldest decisions.</p>
    <p class="front-web">WWW.STONEFIELDPARTNERS.COM</p>
  </section>

  <section class="card card-back">
    <div class="person">
      <h1 class="person-name">DANIEL HALE</h1>
      <p class="person-title">MANAGING DIRECTOR</p>
      <p class="person-office">(LOS ANGELES OFFICE)</p>
    </div>
    <div class="mark"></div>
    <div class="contact">
      <p class="phone">206 555 0147</p>
      <p>dhale@stonefieldpartners.com</p>
      <p>www.stonefieldpartners.com</p>
    </div>
    <div class="office">
      <p class="company">STONEFIELD PARTNERS, INC.</p>
      <p>(HEADQUARTERS)</p>
      <p>218 HARBOR LANE</p>
      <p>SUITE 410</p>
      <p>PORT ALDER, WA 98012</p>
    </div>
  </section>
</body>
</html>
```